Letterhead to Prospective Clients

Create a letterhead (word & canva) that I will use to send letters to prospective clients and also include the Coralwood Estate Partners Logo, My Contact Details and Interchangeable "Suburb". Use the same font and colour pallete

Maris Dulworth | "Suburb" Specialist - Redlands & Surrounds
Mobile: 0417 862 095
Email: MD@CoralwoodEstatePartners.com.au

```html
<!DOCTYPE html>
<html lang="en">
<head>
<meta charset="utf-8">
<title>Coralwood Estate Partners – Letterhead</title>
<link href="https://fonts.googleapis.com/css2?family=Lato:wght@400;700&family=Montserrat:wght@400&display=swap" rel="stylesheet">
<style>
  :root {
    --backdrop: #cdcdcd;
    --paper: #ffffff;
    --navy: #131a3a;
    --tan: #d4a574;
    --ink: #111111;
    --body-grey: #6f6f6f;
    --signature-tone: #ecebea;
  }
  * { margin: 0; padding: 0; box-sizing: border-box; }
  html, body {
    width: 1200px;
    height: 1067px;
    overflow: hidden;
    background: var(--backdrop);
  }
  .letterhead {
    position: absolute;
    left: 240px;
    top: 20px;
    width: 719px;
    height: 1027px;
    background: var(--paper);
    box-shadow: 0 6px 18px rgba(0,0,0,0.18);
    font-family: "Lato", sans-serif;
  }
  .brand {
    position: absolute;
    left: 56px;
    top: 62px;
    font-family: "Montserrat", sans-serif;
    font-weight: 400;
    font-size: 19px;
    letter-spacing: 0.14em;
    color: var(--navy);
    text-transform: uppercase;
    white-space: nowrap;
  }
  .recipient {
    position: absolute;
    left: 56px;
    top: 284px;
    color: var(--ink);
  }
  .recipient-name { font-weight: 700; font-size: 15px; line-height: 20px; }
  .recipient-title { font-weight: 700; font-size: 11px; line-height: 16px; margin-top: 2px; }
  .letter-date {
    position: absolute;
    right: 56px;
    top: 304px;
    font-size: 10.5px;
    color: var(--body-grey);
  }
  .letter-body {
    position: absolute;
    left: 56px;
    top: 358px;
    width: 607px;
    font-size: 10.4px;
    line-height: 17.7px;
    color: var(--body-grey);
    text-align: justify;
    hyphens: auto;
  }
  .letter-body p + p { margin-top: 17.7px; }
  .signature {
    position: absolute;
    left: 56px;
    top: 768px;
    width: 156px;
    height: 38px;
    background: var(--signature-tone);
  }
  .footer-rule {
    position: absolute;
    left: 51px;
    top: 945px;
    width: 614px;
    height: 1px;
    background: var(--tan);
  }
  .agent {
    position: absolute;
    left: 51px;
    top: 960px;
    font-family: "Montserrat", sans-serif;
    color: var(--navy);
  }
  .agent-name { font-size: 13px; line-height: 17px; text-transform: uppercase; letter-spacing: 0.02em; }
  .agent-role { font-size: 10.3px; line-height: 14px; }
  .contact {
    position: absolute;
    left: 459px;
    top: 957px;
    font-family: "Montserrat", sans-serif;
    font-size: 10.3px;
    color: var(--navy);
    list-style: none;
  }
  .contact li { display: flex; align-items: center; height: 17px; }
  .contact svg { width: 9px; height: 9px; margin-right: 5px; fill: var(--tan); }
</style>
</head>
<body>
  <main class="letterhead">
    <div class="brand">Coralwood Estate Partners</div>

    <div class="recipient">
      <div class="recipient-name">Dear. Mrs Elna Grace Whitby</div>
      <div class="recipient-title">Chief Director</div>
    </div>
    <div class="letter-date">Date: 17-June-2025</div>

    <div class="letter-body">
      <p>Lorem ipsum dolor sit amet, consectetur adipiscing elit, sed do eiusmod tempor incididunt ut labore et dolore magna aliqua. Sollicitudin ac orci phasellus egestas tellus rutrum tellus. Euismod elementum nisi quis eleifend quam adipiscing vitae proin sagittis. Egestas sed tempus urna et pharetra pharetra. Quis blandit turpis cursus in hac habitasse. Sed velit dignissim sodales ut eu. Ac auctor augue mauris augue neque. In arcu cursus euismod quis viverra nibh cras pulvinar mattis. Libero justo laoreet sit amet. Felis eget nunc lobortis mattis aliquam faucibus purus in. Pulvinar etiam non quam lacus suspendisse faucibus. Odio tempor orci dapibus ultrices. Velit dignissim sodales ut eu sem integer vitae justo. Fermentum et sollicitudin ac orci phasellus egestas. Pharetra vel turpis nunc eget lorem dolor sed. Sed turpis tincidunt id aliquet risus feugiat in ante. Mus mauris vitae ultricies leo integer malesuada nunc vel. Rhoncus urna neque viverra justo nec ultrices dui. Ut placerat orci nulla pellentesque dignissim enim sit amet.</p>
      <p>Bibendum arcu vitae elementum curabitur vitae nunc. Nunc pulvinar sapien et ligula ullamcorper malesuada. At elementum eu facilisis sed. Erat pellentesque adipiscing commodo elit at imperdiet dui accumsan sit. Nunc scelerisque viverra mauris in aliquam sem fringilla. In vitae turpis massa sed. Volutpat ac tincidunt vitae semper quis lectus nulla at. Massa placerat duis ultricies lacus sed turpis. Dui vivamus arcu felis bibendum ut tristique et egestas. Blandit aliquam etiam erat velit scelerisque in dictum non consectetur. Id neque aliquam vestibulum morbi blandit cursus risus at. Sed egestas egestas fringilla phasellus faucibus scelerisque eleifend donec. Ornare quam viverra orci sagittis eu volutpat odio facilisis. Volutpat sed cras ornare arcu dui vivamus arcu. Interdum consectetur libero id faucibus nisl.</p>
      <p>Viverra mauris in aliquam sem. Mattis molestie a iaculis at erat pellentesque adipiscing commodo elit. Sit amet volutpat consequat mauris nunc. Aliquam nulla facilisi cras fermentum. Sed turpis tincidunt id aliquet risus feugiat. Augue neque gravida in fermentum et sollicitudin ac orci.</p>
    </div>

    <div class="signature" role="img" aria-label="Handwritten signature of Tobin Hale Arden"></div>

    <div class="footer-rule"></div>
    <div class="agent">
      <div class="agent-name">Maris Dulworth</div>
      <div class="agent-role">Specialist - Redlands &amp; Surrounds</div>
    </div>
    <ul class="contact">
      <li>
        <svg viewBox="0 0 10 10" aria-hidden="true"><path d="M1 4 C1 2 2 1.5 5 1.5 C8 1.5 9 2 9 4 L7.5 4.3 L7 3.2 L3 3.2 L2.5 4.3 Z M2.5 5 L3.5 4 L6.5 4 L7.5 5 L8.5 8.5 L1.5 8.5 Z"/></svg>
        0417 862 095
      </li>
      <li>
        <svg viewBox="0 0 10 10" aria-hidden="true"><path d="M0.5 2 L9.5 2 L5 5.5 Z M0.5 3 L5 6.5 L9.5 3 L9.5 8.5 L0.5 8.5 Z"/></svg>
        MD@CoralwoodEstatePartners.com.au
      </li>
    </ul>
  </main>
</body>
</html>
```